Stationary design for IT Consultancy
Stationary Design (Business Cards - Letter Heads - Envelopes - Presentation Folders - Power Point)
Stationary design for IT Consultancy - Information Technology
Creative Brief
Use standard fonts
Optional fonts can be used
Professional
Dean Marlow
Technical Director
14 Brindle Works Oakfield Lane Stoneham Wexshire WX7 2QP
dean.marlow@pivotal-nsg.net
www.pivotal-nsg.net

```html
<!DOCTYPE html>
<html lang="en">
<head>
<meta charset="UTF-8">
<title>Pivotal Network Services Group – Business Card</title>
<link rel="stylesheet" href="https://fonts.googleapis.com/css2?family=Montserrat:wght@700;800&family=Open+Sans:wght@400;600&display=swap">
<style>
  :root {
    --brand-blue: #2f57c2;
    --brand-blue-deep: #1f3f9f;
    --brand-blue-soft: #5b7fd8;
    --card-white: #ffffff;
    --ink: #2a2a2a;
    --backdrop: #e4e6ea;
  }
  * { margin: 0; padding: 0; box-sizing: border-box; }
  html, body {
    width: 1200px; height: 908px; overflow: hidden;
    background: var(--backdrop);
    font-family: "Open Sans", Arial, sans-serif;
  }
  .sheet {
    width: 1200px; height: 908px;
    display: flex; flex-direction: column; align-items: center; justify-content: center;
    gap: 40px;
  }
  .card {
    position: relative;
    width: 700px; height: 400px;
    border-radius: 22px;
    overflow: hidden;
    box-shadow: 0 8px 24px rgba(0,0,0,0.18);
  }
  /* Front */
  .card-front {
    background: linear-gradient(145deg, var(--brand-blue-soft) 0%, var(--brand-blue) 45%, var(--brand-blue-deep) 100%);
    display: flex; align-items: center; justify-content: center;
  }
  .front-brand {
    display: flex; align-items: center; gap: 14px;
    color: var(--card-white);
    font-family: "Montserrat", Arial, sans-serif;
    font-weight: 800; font-size: 44px; letter-spacing: 3px;
  }
  .brand-dot {
    width: 22px; height: 22px; border-radius: 50%;
    background: var(--card-white);
  }
  /* Back */
  .card-back { background: var(--card-white); }
  .card-back .waves { position: absolute; inset: 0; }
  .back-brand {
    position: absolute; left: 60px; top: 132px;
    color: var(--brand-blue);
    font-family: "Montserrat", Arial, sans-serif;
  }
  .back-brand .brand-name {
    display: flex; align-items: center; gap: 10px;
    font-weight: 800; font-size: 38px; letter-spacing: 2px; line-height: 1.15;
  }
  .back-brand .brand-dot { background: var(--brand-blue); width: 18px; height: 18px; }
  .back-brand .brand-tagline {
    margin-top: 2px; margin-left: 28px;
    font-weight: 800; font-size: 12.5px; letter-spacing: 4.4px;
  }
  .person {
    position: absolute; right: 60px; top: 142px; text-align: right;
  }
  .person-name { color: var(--brand-blue); font-size: 22px; font-weight: 600; }
  .person-role { color: var(--ink); font-size: 13px; font-weight: 600; margin-top: 2px; }
  .contact {
    position: absolute; left: 60px; top: 212px;
    color: var(--ink); font-size: 12.5px; line-height: 1.45;
  }
  .contact-address { margin-bottom: 4px; }
  .contact-line { display: flex; align-items: center; gap: 8px; }
  .contact-icon {
    width: 15px; height: 15px; border-radius: 50%;
    background: var(--brand-blue);
    display: flex; align-items: center; justify-content: center;
  }
</style>
</head>
<body>
<main class="sheet">
  <section class="card card-front" aria-label="Card front">
    <div class="front-brand"><span class="brand-dot"></span>PIVOTAL</div>
  </section>

  <section class="card card-back" aria-label="Card back">
    <svg class="waves" width="700" height="400" viewBox="0 0 700 400" aria-hidden="true">
      <path d="M0 0 H700 V28 C520 40 300 70 0 120 Z" fill="var(--brand-blue)"/>
      <path d="M0 126 C300 76 520 46 700 36 V44 C520 54 300 86 0 134 Z" fill="var(--brand-blue-soft)"/>
      <path d="M0 400 V394 C260 392 480 372 700 328 V400 Z" fill="var(--brand-blue)"/>
      <path d="M0 389 C260 387 480 366 700 320 V314 C480 360 260 381 0 383 Z" fill="var(--brand-blue-soft)"/>
    </svg>

    <div class="back-brand">
      <div class="brand-name"><span class="brand-dot"></span>PIVOTAL</div>
      <div class="brand-tagline">NETWORK SERVICES GROUP</div>
    </div>

    <div class="person">
      <div class="person-name">Dean Marlow</div>
      <div class="person-role">Technical Director</div>
    </div>

    <div class="contact">
      <div class="contact-address">
        14 Brindle Works<br>
        Oakfield Lane, Stoneham<br>
        Wexshire<br>
        WX7 2QP
      </div>
      <div class="contact-line">
        <span class="contact-icon">
          <svg width="9" height="9" viewBox="0 0 24 24" aria-hidden="true"><path fill="#fff" d="M6.6 10.8a15.1 15.1 0 0 0 6.6 6.6l2.2-2.2c.3-.3.7-.4 1-.2 1.1.4 2.3.6 3.6.6.6 0 1 .4 1 1V20c0 .6-.4 1-1 1C10.6 21 3 13.4 3 4c0-.6.4-1 1-1h3.5c.6 0 1 .4 1 1 0 1.3.2 2.5.6 3.6.1.3 0 .7-.2 1z"/></svg>
        </span>+44 (0) 7700 900 418
      </div>
      <div class="contact-line">
        <span class="contact-icon">
          <svg width="9" height="9" viewBox="0 0 24 24" aria-hidden="true"><path fill="#fff" d="M3 5h18v14H3z M3 5l9 7 9-7" stroke="#2f57c2" stroke-width="1.5"/></svg>
        </span>dean.marlow@pivotal-nsg.net
      </div>
      <div class="contact-line">
        <span class="contact-icon">
          <svg width="9" height="9" viewBox="0 0 24 24" aria-hidden="true"><circle cx="12" cy="12" r="9" fill="none" stroke="#fff" stroke-width="2.5"/><path d="M3 12h18M12 3c3 3 3 15 0 18M12 3c-3 3-3 15 0 18" fill="none" stroke="#fff" stroke-width="2"/></svg>
        </span>www.pivotal-nsg.net
      </div>
    </div>
  </section>
</main>
</body>
</html>
```